Design for Marketing Consulting Agency - Please see attachments

Looking for a very simple site - 3-5 pages, one with a portfolio page to showcase our work where we can leave comments on it. Looking for modern/clean/impactful design to represent our brand. Here is example of what I like: https://www.trelvon.com/en-us/ logo and mood board and copy for website (minus the portfolio). Prefer black/gray/white with pops of color/imagery that come from the logo. Prefer dark hero, more white and pops of the orange and red for the rest of the site.

Target Market(s)

Small to medium size businesses

Font styles to use
Sans Serif

Colors

Designer to choose only greyscale colors for use in the design.

Requirements
Must have
• Please see mood board. Prefer mostly black/white site with pops of color and imagery.
Nice to have
• Sample portfolio page?
Should not have
• Don't make it look 'futuristic' . Try to make it modern and clean.

```html
<!DOCTYPE html>
<html lang="en">
<head>
<meta charset="utf-8">
<title>Open Lens Marketing</title>
<link href="https://fonts.googleapis.com/css2?family=Lexend:wght@400;500&family=Montserrat:wght@400;500;600&display=swap" rel="stylesheet">
<style>
:root{
  --ink:#111111;
  --footer:#151515;
  --white:#ffffff;
  --accent:#e5432a;
  --cream:#fdf0dc;
  --sky-top:#6a6470;
  --sky-glow:#e48a3a;
  --sky-low:#2b2d37;
}
*{margin:0;padding:0;box-sizing:border-box}
html,body{width:1200px;height:3374px;overflow:hidden;background:var(--white)}
body{position:relative;font-family:'Montserrat',sans-serif;color:var(--ink)}
.abs{position:absolute}
.heading{font-family:'Lexend',sans-serif;font-weight:500;text-transform:uppercase;letter-spacing:.5px}

/* hero */
.hero-photo{left:0;top:0;width:1200px;height:730px;background:linear-gradient(180deg,var(--sky-top) 0%,#9c7466 16%,var(--sky-glow) 30%,#8a5a44 40%,var(--sky-low) 56%,#1f2129 100%)}
.brand{display:flex;align-items:center;gap:12px;color:var(--white);font-family:'Lexend',sans-serif;font-weight:400;text-transform:uppercase}
.brand-mark{width:38px;height:38px;background:var(--white)}
.brand-name{font-size:22px;line-height:21px}
.top-brand{left:172px;top:46px}
.main-nav{right:173px;top:62px;display:flex;gap:17px}
.main-nav a{color:var(--white);text-decoration:none;font-family:'Lexend',sans-serif;font-size:14px;text-transform:uppercase}
.hero-title{left:0;width:1200px;top:478px;text-align:center;color:var(--white);font-size:38px;line-height:46px}

/* about */
.about-title{left:172px;top:846px;font-size:27px}
.about-text{left:172px;top:897px;width:444px;font-size:11.5px;line-height:21px;text-align:justify}
.btn{left:172px;top:1046px;width:173px;height:48px;border-radius:8px;background:var(--accent);color:var(--white);font-family:'Lexend',sans-serif;font-size:13px;display:flex;align-items:center;justify-content:center;text-transform:uppercase}
.photo{border:4px solid var(--white);box-shadow:0 2px 10px rgba(0,0,0,.35)}
.photo-office{left:718px;top:845px;width:309px;height:218px;background:linear-gradient(135deg,#45505c,#9aa6b1 55%,#d8d2cc)}
.photo-desk{left:648px;top:932px;width:249px;height:176px;background:linear-gradient(135deg,#b8752f,#5d7f9a 60%,#c7cdd2)}

/* packages */
.packages-photo{left:0;top:1195px;width:1200px;height:800px;background:linear-gradient(160deg,#242426,#141416 50%,#262422)}
.packages-title{left:0;width:1200px;top:1322px;text-align:center;color:var(--white);font-size:28px}
.package{width:419px;height:445px;border:3px solid var(--white);color:var(--white);top:1410px;text-align:center;overflow:hidden}
.package-a{left:172px}.package-b{left:608px}
.package-arc{position:absolute;left:72px;top:-140px;width:270px;height:220px;border:3px solid var(--white);border-radius:50%}
.package-label{position:absolute;left:0;width:100%;top:20px;font-size:21px}
.package-name{position:absolute;left:0;width:100%;top:104px;font-size:19px}
.price{position:absolute;left:50%;transform:translateX(-50%);top:148px;padding:0 9px;height:47px;border-radius:8px;background:var(--accent);font-weight:600;font-size:15.5px;display:flex;align-items:center}
.meetings{position:absolute;left:0;width:100%;top:210px;font-size:15px;font-weight:500}
.package-rule{position:absolute;left:0;width:100%;top:265px;border-top:3px solid var(--white)}
.output{position:absolute;left:0;width:100%;top:290px;font-size:14px;line-height:21px}

/* services */
.services-title{left:0;width:1200px;top:2056px;text-align:center;font-size:28px}
.service-img{width:243px;height:207px;top:2143px;border:3px solid var(--white);box-shadow:0 2px 10px rgba(0,0,0,.3)}
.service-label{width:243px;height:105px;top:2280px;background:var(--white);box-shadow:0 2px 10px rgba(0,0,0,.2);font-family:'Lexend',sans-serif;font-size:15px;line-height:21px;text-transform:uppercase;display:flex;align-items:center;justify-content:center;text-align:center;padding:0 8px}

/* team */
.team-bg{left:0;top:2470px;width:1200px;height:435px;background:var(--cream)}
.team-title{left:0;width:1200px;top:2624px;text-align:center;font-size:28px}
.team-text{left:172px;width:856px;top:2688px;text-align:center;font-size:12px;line-height:21px}

/* footer */
.footer-bg{left:0;top:2905px;width:1200px;height:469px;background:var(--footer)}
.footer-brand{left:0;width:1200px;top:3068px;justify-content:center;gap:18px}
.footer-brand .brand-mark{width:64px;height:64px}
.footer-brand .brand-name{font-size:38px;line-height:38px}
.footer-nav{left:0;width:1200px;top:3232px;display:flex;justify-content:center;gap:16px;color:var(--white);font-family:'Lexend',sans-serif;font-size:16px;text-transform:uppercase}
.footer-nav a{color:var(--white);text-decoration:none}
.footer-rule{left:172px;width:856px;top:3294px;border-top:1px solid #8a8a8a}
.copyright{left:0;width:1200px;top:3328px;text-align:center;color:var(--white);font-size:14px}
</style>
</head>
<body>

<!-- hero -->
<div class="abs hero-photo" role="img" aria-label="Mountain range at sunset with an orange sky"></div>
<div class="abs brand top-brand"><span class="brand-mark"></span><span class="brand-name">Open Lens<br>Marketing</span></div>
<nav class="abs main-nav"><a href="#">Home</a><a href="#">Who are we?</a><a href="#">Our Packages</a><a href="#">Our Work</a><a href="#">Team</a><a href="#">Contact</a></nav>
<h1 class="abs heading hero-title">We deliver simple, clear, and impactful<br>messaging and designs</h1>

<!-- about -->
<h2 class="abs heading about-title">Who are we?</h2>
<p class="abs about-text">Open Lens Marketing is a Marketing Agency that delivers a breadth of services from brand/rebrand, strategy, design, and web to digital and print marketing campaigns and trade shows. We bring over 20 years of experience in marketing for both B2B to B2C organizations ranging from 5M to over 200M. We're passionate. We're poignant. We know what you're trying to say, and so will your customers.</p>
<div class="abs btn">Learn more about</div>
<div class="abs photo photo-office" role="img" aria-label="Colleagues talking in a bright modern office"></div>
<div class="abs photo photo-desk" role="img" aria-label="Man on a phone call at a laptop"></div>

<!-- packages -->
<div class="abs packages-photo" role="img" aria-label="Dim photo of a team meeting"></div>
<h2 class="abs heading packages-title">Our Packages</h2>

<div class="abs package package-a">
  <div class="package-arc"></div>
  <div class="package-label heading">The Packages</div>
  <div class="package-name heading">Website &amp; Messaging Facelift</div>
  <div class="price">$3000 -$4000</div>
  <div class="meetings">Meetings necessary: 4-5 hours</div>
  <div class="package-rule"></div>
  <div class="output">The output:<br>Two homepage mockups.<br>One mood board.<br>Two versions of value proposition messaging – x words<br>See Case Study (Gritworks Labs)</div>
</div>
<div class="abs package package-b">
  <div class="package-arc"></div>
  <div class="package-label heading">The Packages</div>
  <div class="package-name heading">Simple Brand Rebuild</div>
  <div class="price">$5000-$6000</div>
  <div class="meetings">Meetings necessary: 6-7 hours</div>
  <div class="package-rule"></div>
  <div class="output">The output:<br>5 logo concepts<br>Two homepage mockups<br>One brand storyboard<br>Two versions of value proposition messaging<br>See example case study (my side hustle)</div>
</div>

<!-- services -->
<h2 class="abs heading services-title">Additional Services Offered</h2>
<div class="abs service-img" style="left:172px;background:linear-gradient(135deg,#d6cbbf,#8a6e58 60%,#cfd3d6)" role="img" aria-label="Team brainstorming around a table"></div>
<div class="abs service-label" style="left:187px">Strategic consulting on growth strategies and building teams</div>
<div class="abs service-img" style="left:470px;background:linear-gradient(135deg,#2e3a4c,#6f88a8 55%,#d9d3cf)" role="img" aria-label="Hands typing on a laptop with floating screens"></div>
<div class="abs service-label" style="left:485px">Trade show management and booth designs</div>
<div class="abs service-img" style="left:768px;background:linear-gradient(135deg,#e8e4de,#394459 60%,#c9c2b8)" role="img" aria-label="Two colleagues reviewing work together"></div>
<div class="abs service-label" style="left:783px">Email marketing campaigns</div>

<!-- team -->
<div class="abs team-bg" role="img" aria-label="Cream background with faint topographic pattern"></div>
<h2 class="abs heading team-title">The Team</h2>
<p class="abs team-text">Open Lens Marketing is run and managed by Dana Whitcombe. It has a team of experts from content creation to graphic design and digital marketing. Dana is a passionate marketing visionary with 20+ years of experience leading direct and channel marketing teams and creating powerful and effective multi-channel marketing strategies and campaigns. She has experience working with businesses ranging from 100k to Fortune 500 companies, Dana has her master's degree from Harwell College and her undergraduate degree from Larchmont University.</p>

<!-- footer -->
<div class="abs footer-bg"></div>
<div class="abs brand footer-brand"><span class="brand-mark"></span><span class="brand-name">Open Lens<br>Marketing</span></div>
<nav class="abs footer-nav"><a href="#">Home</a><span>|</span><a href="#">Who are we?</a><span>|</span><a href="#">Our Packages</a><span>|</span><a href="#">Our Work</a><span>|</span><a href="#">Team</a><span>|</span><a href="#">Contact</a></nav>
<div class="abs footer-rule"></div>
<p class="abs copyright">Copyrights @ 2022 Open Lens Marketing</p>

</body>
</html>
```